Business Card Design Project

I would like to redesign our business cards and change the look and feel of our marketing material, but maintain the same basic identity of our current logo.
It is my belief that it could be much better.
You can view our website at kducn.com

   

I was looking for a completely different look.  Something much more hip and cool looking.  You can change the colors.

I like this look and feel

 http://www.hudlawfirm.com

 But obviously don’t want to copy them exactly.

 

For the back just leave the last point.

“Focus on Your Business, and We’ll Focus on Your Claim”

I want there to be space for someone to write on.

                                                                    

                                       

I like this look and feel

 http://www.hudlawfirm.com

```html
<!DOCTYPE html>
<html lang="en">
<head>
<meta charset="utf-8">
<title>Crestline Claim Advisors – Business Card</title>
<link rel="stylesheet" href="https://fonts.googleapis.com/css2?family=Fira+Sans+Condensed:wght@300;400;600&display=swap">
<style>
  :root {
    --stage: #2b3346;
    --card-navy: #0b1030;
    --card-navy-deep: #050818;
    --ink-white: #ffffff;
    --ink-blue: #3d7dff;
    --glow-core: #6fb4ff;
    --glow-mid: #1f5cff;
    --glow-edge: rgba(10, 30, 120, 0);
    --back-paper: #ffffff;
    --back-ink: #1a2a6c;
  }
  * { box-sizing: border-box; margin: 0; padding: 0; }
  html, body {
    width: 1200px;
    height: 900px;
    overflow: hidden;
    background: var(--stage);
    font-family: "Fira Sans Condensed", "Arial Narrow", sans-serif;
  }
  .sheet {
    width: 1200px;
    height: 900px;
    display: flex;
    align-items: center;
    justify-content: center;
    gap: 40px;
  }
  .card {
    position: relative;
    width: 540px;
    height: 309px;
    border-radius: 4px;
    overflow: hidden;
    box-shadow: 0 14px 36px rgba(0, 0, 0, 0.45);
  }
  .card--front {
    background: radial-gradient(ellipse at 70% 55%, var(--card-navy) 0%, var(--card-navy-deep) 100%);
    color: var(--ink-white);
  }
  .brand {
    position: absolute;
    top: 26px;
    left: 26px;
    display: flex;
    align-items: center;
    gap: 12px;
  }
  .brand__dot {
    width: 34px;
    height: 34px;
    border-radius: 50%;
    background: var(--ink-white);
  }
  .brand__name {
    font-size: 15px;
    font-weight: 400;
    letter-spacing: 0.06em;
    text-transform: uppercase;
    color: var(--ink-white);
  }
  .person {
    position: absolute;
    left: 66px;
    top: 92px;
  }
  .person__name {
    font-size: 30px;
    font-weight: 600;
    color: var(--ink-white);
    letter-spacing: 0.01em;
  }
  .contact {
    margin-top: 16px;
    list-style: none;
    font-size: 13px;
    font-weight: 300;
    line-height: 1.45;
    color: var(--ink-blue);
  }
  .address {
    margin-top: 14px;
    font-style: normal;
    font-size: 13px;
    font-weight: 300;
    line-height: 1.45;
    color: var(--ink-blue);
  }
  .brain-art {
    position: absolute;
    right: 34px;
    top: 92px;
    width: 180px;
    height: 150px;
    border-radius: 50%;
    background: radial-gradient(ellipse at 50% 50%, var(--glow-core) 0%, var(--glow-mid) 45%, var(--glow-edge) 72%);
  }
  .card--back {
    background: var(--back-paper);
    display: flex;
    align-items: center;
    justify-content: center;
  }
  .tagline {
    text-align: center;
    font-size: 14px;
    font-weight: 400;
    line-height: 1.4;
    letter-spacing: 0.04em;
    color: var(--back-ink);
  }
</style>
</head>
<body>
  <main class="sheet">
    <section class="card card--front" aria-label="Card front">
      <header class="brand">
        <span class="brand__dot"></span>
        <span class="brand__name">Crestline Claim Advisors</span>
      </header>
      <div class="person">
        <h1 class="person__name">Daniel Moreau</h1>
        <ul class="contact">
          <li>office: 555.014.2290</li>
          <li>cell: 555.019.7731</li>
          <li>dan@kducn.com</li>
          <li>www.kducn.com</li>
        </ul>
        <address class="address">48 Linden Avenue<br>Westvale, NY 10999</address>
      </div>
      <div class="brain-art" role="img" aria-label="Glowing blue illustration of a human brain"></div>
    </section>

    <section class="card card--back" aria-label="Card back">
      <p class="tagline">Run Your Business<br>We'll Handle Your Case</p>
    </section>
  </main>
</body>
</html>
```